We want a business card/punch card for our business. We are including examples of our current business card (we like the front of our business card and not looking to remake it). We need only back side to be designed in form of a punch card (we are including a sample of the punch card we made, but are unsatisfied). For each $180 spend (9 punches) our clients have $20 off.

Colors
886aae

```html
<!DOCTYPE html>
<html lang="en">
<head>
<meta charset="utf-8">
<title>Lotus Path – Business Card &amp; Punch Card</title>
<link href="https://fonts.googleapis.com/css2?family=Crimson+Text:wght@600;700&family=Roboto:wght@300;400&display=swap" rel="stylesheet">
<style>
  :root {
    --purple: #5e2d8f;
    --lavender: #886aae;
    --blue: #5563b0;
    --blue-light: #8a9bd6;
    --mist: #b7c3e8;
    --ink: #1b1b1d;
    --white: #ffffff;
    --serif: "Crimson Text", Georgia, serif;
    --sans: "Roboto", Arial, sans-serif;
  }
  * { box-sizing: border-box; margin: 0; padding: 0; }
  html, body { width: 1200px; height: 1200px; overflow: hidden; background: var(--white); }
  .canvas { position: relative; width: 1200px; height: 1200px; }

  /* Brand name, standalone */
  .brand-standalone {
    position: absolute; left: 64px; top: 150px;
    display: flex; align-items: center; gap: 12px;
    font-family: var(--serif); font-weight: 700; font-size: 44px; color: var(--blue);
  }
  .brand-dot { width: 18px; height: 18px; border-radius: 50%; background: var(--purple); }

  .card { position: absolute; box-shadow: 3px 4px 8px rgba(0,0,0,.35); overflow: hidden; }

  /* Front */
  .card-front { left: 372px; top: 134px; width: 758px; height: 440px; }
  .front-pattern {
    position: absolute; inset: 0;
    background: radial-gradient(ellipse at 36% 56%, #f2f4fc 0%, #d3dbf2 40%, var(--mist) 75%, #a9b6e2 100%);
  }
  .front-swoosh { position: absolute; inset: 0; width: 100%; height: 100%; }
  .front-brand {
    position: absolute; left: 80px; top: 290px;
    display: flex; align-items: center; gap: 12px;
    font-family: var(--serif); font-weight: 700; font-size: 56px; color: var(--blue);
  }
  .front-brand .brand-dot { width: 22px; height: 22px; }
  .contact {
    position: absolute; right: 70px; text-align: right;
    font-family: var(--sans); font-weight: 300; color: var(--white);
  }
  .contact-person { top: 76px; font-size: 24px; line-height: 30px; }
  .contact-person .name { font-weight: 400; }
  .contact-web { top: 272px; font-size: 19px; line-height: 25px; }
  .contact-social { top: 331px; font-size: 19px; line-height: 32px; }

  /* Back */
  .card-back { left: 372px; top: 630px; width: 770px; height: 450px; background: var(--blue); }
  .divider { position: absolute; top: 0; bottom: 0; width: 5px; background: var(--ink); }
  .divider-left { left: 260px; }
  .divider-right { left: 506px; }
  .punch-panel { position: absolute; top: 0; bottom: 0; left: 265px; width: 241px; background: var(--white); }

  .service {
    position: absolute; height: 48px;
    background: var(--ink); color: var(--white);
    display: flex; align-items: center; justify-content: center;
    font-family: var(--serif); font-weight: 700; font-size: 23px;
  }
  .service-left { left: 2px; width: 243px; }
  .service-right { left: 529px; width: 241px; }
  .spaced-wide { letter-spacing: 0.95em; padding-left: 0.95em; }
  .spaced { letter-spacing: 0.55em; padding-left: 0.55em; }
  .spaced-light { letter-spacing: 0.3em; padding-left: 0.3em; }
  .service-small { font-size: 17px; }

  .punch {
    position: absolute; width: 82px; height: 48px;
    background: var(--ink); color: var(--blue);
    display: flex; align-items: center; justify-content: center;
    font-family: var(--serif); font-weight: 700; font-size: 27px;
  }
  .punch-note {
    position: absolute; left: 265px; width: 241px; top: 320px;
    text-align: center; font-family: var(--serif); font-weight: 600;
    font-size: 13.5px; line-height: 25px; color: var(--ink);
  }
  .punch-note .highlight { color: var(--blue); }
</style>
</head>
<body>
<main class="canvas">

  <div class="brand-standalone"><span class="brand-dot"></span>Lotus Path</div>

  <section class="card card-front" aria-label="Business card front">
    <div class="front-pattern" role="img" aria-label="Soft pale blue mandala pattern background"></div>
    <svg class="front-swoosh" viewBox="0 0 947 551" preserveAspectRatio="none" aria-hidden="true">
      <path d="M590 0 C670 160 470 300 468 551 L947 551 L947 0 Z" fill="var(--blue-light)"/>
      <path d="M632 0 C700 170 490 300 488 551 L947 551 L947 0 Z" fill="var(--blue)"/>
      <path d="M640 0 C672 130 600 220 540 290 C660 240 800 220 947 238 L947 0 Z" fill="var(--purple)"/>
    </svg>
    <div class="front-brand"><span class="brand-dot"></span>Lotus Path</div>
    <div class="contact contact-person">
      <div class="name">Mira Solenne</div>
      <div>555-014-2290</div>
    </div>
    <div class="contact contact-web">
      <div>www.lotuspathstudio.com</div>
      <div>hello@lotuspathstudio.com</div>
    </div>
    <div class="contact contact-social">
      <div>Friendbook.com/LotusPathStudio</div>
      <div>Gatherup.com/Lotus-Path</div>
    </div>
  </section>

  <section class="card card-back" aria-label="Punch card back">
    <div class="punch-panel"></div>
    <div class="divider divider-left"></div>
    <div class="divider divider-right"></div>

    <div class="service service-left spaced-wide" style="top:49px">Tao</div>
    <div class="service service-left spaced" style="top:105px">Reiki</div>
    <div class="service service-left spaced" style="top:161px">Tantra</div>
    <div class="service service-left spaced" style="top:217px">Tai Chi</div>
    <div class="service service-left" style="top:273px">Sexual Healing</div>
    <div class="service service-left" style="top:329px">Sacred Sexuality</div>

    <div class="service service-right spaced" style="top:49px">Yoaga</div>
    <div class="service service-right spaced-light" style="top:105px">Rituals</div>
    <div class="service service-right" style="top:161px">Sound Heali</div>
    <div class="service service-right" style="top:217px">Partners Yoga</div>
    <div class="service service-right" style="top:273px">Energy Work</div>
    <div class="service service-right service-small" style="top:329px">Four Hands Massage</div>

    <div class="punch" style="left:287px;top:46px">$20</div>
    <div class="punch" style="left:400px;top:46px">$20</div>
    <div class="punch" style="left:287px;top:129px">$20</div>
    <div class="punch" style="left:400px;top:129px">$20</div>
    <div class="punch" style="left:287px;top:210px">$20</div>
    <div class="punch" style="left:400px;top:210px">$20</div>

    <p class="punch-note">Filling This Card With 9 Punches<br>Give You <span class="highlight">$20 Off</span> Your Next Visit</p>
  </section>

</main>
</body>
</html>
```